Tinselwick Flyer

Require a flyer for our pet photography business. I have uploaded a very poor attempt I have made at designing one. the size is to be DL and to be one page, but coloured on both sides. I have included the template to which the design is to fit.

Target Market(s)

Pet owners

Font styles to use
Sans Serif

Requirements
Must have
• I have included snap shots from our webdesign. The flyer design should be complimentary to the web design. Please use wording on the flyer front from the files called webscreenshots
Nice to have
• The back: a portfolio of the images on the back side with the logo and the website.
• The front: On the front side we would like a maximum of three photos (different to the ones used on the back) with the writing from the screen shots and the logo.
• check the names of the photos to be put on the flyer, I have called them back and front as appropriate.

```html
<!DOCTYPE html>
<html lang="en">
<head>
<meta charset="utf-8">
<title>Tinselwick Pet Photography – DL Flyer</title>
<link rel="stylesheet" href="https://fonts.googleapis.com/css2?family=Oswald:wght@400;500;600&family=Abel&display=swap">
<style>
  :root {
    --page-bg: #ffffff;
    --card-white: #ffffff;
    --sky: #aec4e0;
    --slate: #6f8ea9;
    --rose: #e8908d;
    --text-grey: #7d7f84;
    --brand-red: #a3161b;
    --white: #ffffff;
  }
  * { box-sizing: border-box; margin: 0; padding: 0; }
  html, body { width: 1200px; height: 982px; overflow: hidden; background: var(--page-bg); }
  body { position: relative; font-family: "Abel", sans-serif; color: var(--text-grey); }

  .flyer-side {
    position: absolute;
    width: 780px;
    height: 400px;
    background: var(--card-white);
    box-shadow: 0 8px 22px rgba(0,0,0,0.22);
    overflow: hidden;
  }
  .flyer-front { left: 200px; top: 70px; }
  .flyer-back { left: 220px; top: 500px; }

  /* Front */
  .front-panel {
    position: absolute;
    left: 18px; top: 18px; right: 18px; bottom: 18px;
    background: var(--sky);
  }
  .brand {
    position: absolute;
    left: 30px; top: 66px;
    display: flex; align-items: center; gap: 7px;
  }
  .brand-dot { width: 18px; height: 18px; border-radius: 50%; background: var(--brand-red); flex: none; }
  .brand-name {
    font-family: "Oswald", sans-serif;
    font-weight: 600;
    font-size: 15px;
    letter-spacing: 0.4px;
    color: var(--brand-red);
    text-transform: uppercase;
  }
  .headline {
    position: absolute;
    left: 30px; top: 134px;
    font-family: "Oswald", sans-serif;
    font-weight: 600;
    color: var(--white);
    text-transform: uppercase;
    line-height: 1.08;
  }
  .headline-main { display: block; font-size: 31px; }
  .headline-sub { display: block; font-size: 23px; margin-left: 6px; }
  .steps {
    position: absolute;
    left: 40px; top: 232px;
    list-style: none;
    border-left: 4px solid var(--text-grey);
    padding-left: 6px;
    font-family: "Oswald", sans-serif;
    font-weight: 400;
    font-size: 15px;
    line-height: 1.15;
    color: var(--text-grey);
    width: 180px;
  }
  .find-more {
    position: absolute;
    left: 42px; top: 316px;
    font-family: "Oswald", sans-serif;
    font-weight: 400;
    font-size: 15px;
    color: var(--text-grey);
  }
  .photo { position: absolute; }
  .photo-dog-hat {
    left: 248px; top: 100px; width: 146px; height: 232px;
    background:
      radial-gradient(ellipse 60% 25% at 50% 20%, #a9adb3 0%, transparent 100%),
      radial-gradient(ellipse 70% 45% at 55% 62%, #efe6d6 0%, transparent 100%),
      linear-gradient(180deg, #d9dde1, #c5cbd1);
  }
  .photo-cat {
    left: 396px; top: 26px; width: 172px; height: 280px;
    background:
      radial-gradient(ellipse 55% 45% at 62% 48%, #8e8478 0%, #5a534c 45%, transparent 80%),
      var(--text-grey) linear-gradient(180deg, #141415, #1b1b1c);
  }
  .photo-poodle {
    left: 574px; top: 34px; width: 138px; height: 268px;
    background:
      radial-gradient(ellipse 55% 55% at 50% 55%, #f7f2ef 0%, #f1e4e1 45%, transparent 75%),
      linear-gradient(180deg, #f0cbc5, #e8b6b0);
  }

  /* Back */
  .back-copy {
    position: absolute;
    left: 40px; top: 66px;
    width: 262px;
    font-family: "Oswald", sans-serif;
    font-weight: 400;
    font-size: 11.5px;
    line-height: 1.2;
    color: var(--text-grey);
  }
  .back-copy p { margin-bottom: 11px; }
  .credentials {
    position: absolute;
    left: 54px; top: 296px;
    display: flex; align-items: flex-start; gap: 12px;
  }
  .badge { width: 64px; height: 64px; border-radius: 50%; border: 1.5px solid var(--text-grey); background: var(--card-white); flex: none; }
  .contact { font-family: "Abel", sans-serif; font-size: 9px; line-height: 1.75; color: var(--text-grey); }
  .contact .web { font-family: "Oswald", sans-serif; font-weight: 400; font-size: 12px; margin-top: 3px; }
  .portfolio {
    position: absolute;
    left: 314px; top: 36px;
    display: grid;
    grid-template-columns: repeat(4, 96px);
    grid-template-rows: repeat(3, 100px);
    gap: 4px;
  }
  .tile-sky { background: var(--sky); }
  .tile-rose { background: var(--rose); }
  .tile-slate { background: var(--slate); }
  .tile-mastiff {
    background:
      radial-gradient(ellipse 60% 55% at 50% 55%, #b8895a 0%, #8a6440 50%, transparent 85%),
      linear-gradient(180deg, #e6dcd6, #cdb9ad);
  }
  .tile-owner-cat {
    background:
      radial-gradient(ellipse 50% 55% at 55% 65%, #f1ece6 0%, #5b4a44 55%, transparent 85%),
      linear-gradient(180deg, #d9c9b4, #c7b39b);
  }
  .tile-horse {
    background:
      radial-gradient(ellipse 45% 60% at 30% 55%, #6e3e26 0%, transparent 90%),
      radial-gradient(ellipse 40% 50% at 75% 40%, #e6c9a0 0%, transparent 90%),
      linear-gradient(160deg, #caa071, #8c5e3e);
  }
  .tile-fluffy-dog {
    background:
      radial-gradient(ellipse 40% 50% at 50% 55%, #e6dcd0 0%, #9b8a78 45%, transparent 80%),
      linear-gradient(180deg, #2f2823, #3d322b);
  }
  .tile-cat {
    background:
      radial-gradient(ellipse 40% 50% at 45% 60%, #e9e6e2 0%, #8a8078 50%, transparent 85%),
      linear-gradient(160deg, #8a6c52, #5e4a3a);
  }
  .tile-owner-dog {
    background:
      radial-gradient(ellipse 45% 40% at 65% 55%, #d9cfc4 0%, transparent 90%),
      radial-gradient(ellipse 30% 40% at 30% 55%, #2a2a2a 0%, transparent 90%),
      linear-gradient(180deg, #9aa27a, #6d8050);
  }
</style>
</head>
<body>

<section class="flyer-side flyer-front">
  <div class="front-panel">
    <div class="brand">
      <span class="brand-dot"></span>
      <span class="brand-name">Tinselwick Pet Photography</span>
    </div>
    <h1 class="headline">
      <span class="headline-main">It´s Pawsome!</span>
      <span class="headline-sub">And so simple:</span>
    </h1>
    <ol class="steps">
      <li>1. Let´s Chat</li>
      <li>2. Pick a Date</li>
      <li>3. Turn up for an Awesome Experience</li>
    </ol>
    <p class="find-more">Find out more</p>
    <div class="photo photo-dog-hat" role="img" aria-label="Shaggy dog wearing a knitted grey hat and scarf"></div>
    <div class="photo photo-cat" role="img" aria-label="Long-haired tabby cat peeking in from the side on black"></div>
    <div class="photo photo-poodle" role="img" aria-label="White poodle with pink ears and flower collar on pink backdrop"></div>
  </div>
</section>

<section class="flyer-side flyer-back">
  <div class="back-copy">
    <p>Be At Ease<br>In Studio | On Location | At Home</p>
    <p>All session are available to ensure you and your pet are comfortable<br>(Note: At this time all Tinselwick Pet Photography is only available in studio)</p>
    <p>You Get it All!<br>Beautifully printed photographs on art paper along with the digital files.</p>
    <p>Fun Quirky &amp; Beautiful Pet Photography<br>Now Available in Brookhaven</p>
  </div>
  <div class="credentials">
    <div class="badge"></div>
    <div class="contact">
      <div>Award Winning Pet Loving Photographers</div>
      <div>Marcus Holt &amp; Fiona Reyes</div>
      <div>Phone: Fiona 0400 555 218</div>
      <div>hello@tinselwickpets.com</div>
      <div class="web">www.tinselwickpets.com</div>
    </div>
  </div>
  <div class="portfolio">
    <div class="tile-mastiff" role="img" aria-label="Mastiff dog portrait"></div>
    <div class="tile-sky"></div>
    <div class="tile-owner-cat" role="img" aria-label="Woman holding a cat"></div>
    <div class="tile-sky"></div>
    <div class="tile-sky"></div>
    <div class="tile-horse" role="img" aria-label="Girl with her horse at sunset"></div>
    <div class="tile-rose"></div>
    <div class="tile-fluffy-dog" role="img" aria-label="Small fluffy dog on dark background"></div>
    <div class="tile-cat" role="img" aria-label="Grey and white cat sitting in a basket"></div>
    <div class="tile-slate"></div>
    <div class="tile-owner-dog" role="img" aria-label="Woman sitting on grass with her dog"></div>
    <div class="tile-sky"></div>
  </div>
</section>

</body>
</html>
```